nutrition company business card

I would like to have a business card that has two sides, one being the green color from the Company name on the logo. I am open to ideas and looks that work with my logo. I like the idea of having a negative image of the tree on the green side.

For my information on the card I must have:
Helen Dunmore
415-555-0183
helendunmore@mailvista.net

This area will need to be updated once I complete my schooling.

Reason: I need to extend my deadline by one day as I have been sick the last week and not had time to review all the new designs. Thank you.

Nutrition

• I would like to have a business card that has two sides, one being the green color from the Company name on the logo. I am open to ideas and looks that work with my logo. I like the idea of having a negative image of the tree on the green side.
• For my information on the card I must have:
• Helen Dunmore
• 415-555-0183
• helendunmore@mailvista.net
• This area will need to be updated once I complete my schooling.

```html
<!DOCTYPE html>
<html lang="en">
<head>
<meta charset="utf-8">
<title>Calder Nutrition – Business Card</title>
<link href="https://fonts.googleapis.com/css2?family=Open+Sans:wght@400;600&display=swap" rel="stylesheet">
<style>
  :root {
    --leaf-green: #74b935;
    --paper: #ffffff;
    --bark-brown: #6b5a4e;
    --backdrop: #e9e7e2;
  }
  * { margin: 0; padding: 0; box-sizing: border-box; }
  html, body {
    width: 1200px; height: 857px; overflow: hidden;
    background: var(--backdrop);
  }
  .canvas {
    position: relative; width: 1200px; height: 857px;
    display: flex; align-items: center; justify-content: center; gap: 60px;
  }
  .card {
    position: relative; width: 525px; height: 300px;
    overflow: hidden; border-radius: 3px;
    box-shadow: 0 6px 18px rgba(0,0,0,0.15);
    font-family: "Open Sans", sans-serif;
  }

  /* ---------- front (green) ---------- */
  .card-front { background: var(--leaf-green); }
  .card-front .brand {
    position: absolute; left: 0; right: 0; top: 70px;
    display: flex; flex-direction: column; align-items: center;
    color: var(--paper);
  }
  .brand-mark {
    width: 62px; height: 62px; border-radius: 50%;
    border: 3px solid var(--paper); margin-bottom: 10px;
  }
  .brand-name {
    font-weight: 400; font-size: 32px; line-height: 1.1;
  }
  .brand-tagline {
    font-weight: 400; font-size: 16px; line-height: 1.3; letter-spacing: 0.4px;
  }

  /* ---------- back (white + green band) ---------- */
  .card-back { background: var(--paper); }
  .card-back .contact-band {
    position: absolute; left: 0; right: 0; top: 138px; height: 162px;
    background: var(--leaf-green);
  }
  .card-back .brand {
    position: absolute; left: 34px; top: 20px;
    display: flex; flex-direction: column; align-items: center;
  }
  .card-back .brand-mark {
    border-color: var(--bark-brown); width: 52px; height: 52px;
    margin-bottom: 6px;
  }
  .card-back .brand-name { color: var(--leaf-green); font-size: 26px; }
  .card-back .brand-tagline { color: var(--bark-brown); font-size: 13px; }

  .contact {
    position: absolute; left: 34px; top: 160px; color: var(--paper);
  }
  .contact-name { font-weight: 600; font-size: 22px; margin-bottom: 10px; }
  .contact-line {
    display: flex; align-items: center; gap: 8px;
    font-size: 13px; margin-bottom: 6px;
  }
  .contact-line svg { width: 11px; height: 11px; fill: var(--paper); }
</style>
</head>
<body>
<main class="canvas">

  <section class="card card-front" aria-label="Card front">
    <div class="brand">
      <div class="brand-mark" aria-hidden="true"></div>
      <div class="brand-name">Calder Nutrition</div>
      <div class="brand-tagline">simple meals for every home</div>
    </div>
  </section>

  <section class="card card-back" aria-label="Card back">
    <div class="contact-band"></div>
    <div class="brand">
      <div class="brand-mark" aria-hidden="true"></div>
      <div class="brand-name">Calder Nutrition</div>
      <div class="brand-tagline">simple meals for every home</div>
    </div>
    <div class="contact">
      <div class="contact-name">Maren Colby</div>
      <div class="contact-line">
        <svg viewBox="0 0 24 24" aria-hidden="true"><path d="M6.6 10.8a15.1 15.1 0 0 0 6.6 6.6l2.2-2.2a1 1 0 0 1 1-.25 11.4 11.4 0 0 0 3.6.57 1 1 0 0 1 1 1V20a1 1 0 0 1-1 1A17 17 0 0 1 3 4a1 1 0 0 1 1-1h3.5a1 1 0 0 1 1 1 11.4 11.4 0 0 0 .57 3.6 1 1 0 0 1-.25 1z"/></svg>
        <span>415-555-0183</span>
      </div>
      <div class="contact-line">
        <svg viewBox="0 0 24 24" aria-hidden="true"><path d="M2 5h20v14H2z M2 5l10 8 10-8" stroke="#74b935" stroke-width="1.5"/></svg>
        <span>marencolby@mailvista.net</span>
      </div>
    </div>
  </section>

</main>
</body>
</html>
```